Orbit Field Athletics - "Vuemarq of Sports" design needed

We need a web design created for Orbit Field Athletics. This includes these separate page
The Site map needed has been updated and available to you in Adobe Muse.....
1) Landing Page / Home page
2) Authentication login / Sign up page
3) After logged in - All Content Page
- IE: Vuemarq
4) Once a thumbnail is selected - Content player and other similar content thumbnails
- IE: Vuemarq
4) Generic pages for content fields - terms / policies / contact us / information / etc
5) Generic pages for customer input content fields - My profile / payment / account information / cancellation page
Important for Project Selection.....
A - Design needs to be for Desktop and Mobile.
B - The best example I can point to - that so long as skinned similarly to our
branding at OrbitFieldAthletics is vuemarq.example or KRDV MAX or Tavo
C - Final design needs to be in layered in PSD and AI
D - Attached is our old design that needs an updated concept. Format has been
done in Adobe Muse.

```html
<!DOCTYPE html>
<html lang="en">
<head>
<meta charset="utf-8">
<title>Orbit Field Athletics — Login</title>
<link rel="stylesheet" href="https://fonts.googleapis.com/css2?family=Montserrat:wght@600;800&family=Open+Sans:wght@400&display=swap">
<style>
  :root {
    --page-bg: #0b0b0c;
    --brand-red: #e3001b;
    --text-white: #ffffff;
    --field-border: #cfcfcf;
    --panel-rim: rgba(70, 70, 72, 0.75);
    --panel-fill: rgba(14, 14, 15, 0.78);
  }
  * { margin: 0; padding: 0; box-sizing: border-box; }
  html, body {
    width: 1200px;
    height: 760px;
    overflow: hidden;
    background: var(--page-bg);
  }
  .login-page {
    position: relative;
    width: 1200px;
    height: 760px;
    overflow: hidden;
  }
  .hero-backdrop {
    position: absolute;
    inset: 0;
    background:
      radial-gradient(ellipse 170px 90px at 290px 260px, rgba(120,120,125,0.35), transparent 70%),
      radial-gradient(ellipse 260px 200px at 830px 520px, rgba(92,84,30,0.45), transparent 75%),
      radial-gradient(ellipse 60px 60px at 838px 110px, rgba(110,110,110,0.35), transparent 80%),
      linear-gradient(180deg, #121213 0%, #17171a 45%, #1b1713 75%, #0f0e0d 100%);
  }
  .brand {
    position: absolute;
    left: 373px;
    top: 108px;
    width: 270px;
    display: flex;
    align-items: center;
    justify-content: center;
    gap: 10px;
  }
  .brand-mark {
    width: 14px;
    height: 14px;
    background: var(--brand-red);
    flex: none;
  }
  .brand-name {
    font-family: "Montserrat", sans-serif;
    font-weight: 600;
    font-size: 22px;
    letter-spacing: 0.5px;
    color: var(--text-white);
    white-space: nowrap;
  }
  .login-frame {
    position: absolute;
    left: 376px;
    top: 246px;
    width: 422px;
    height: 344px;
    background: var(--panel-rim);
  }
  .login-frame .corners {
    position: absolute;
    inset: 0;
    width: 100%;
    height: 100%;
    overflow: visible;
  }
  .login-panel {
    position: absolute;
    left: 13px;
    top: 12px;
    width: 397px;
    height: 320px;
    background: var(--panel-fill);
  }
  .login-form {
    position: absolute;
    left: 36px;
    top: 56px;
    width: 328px;
  }
  .field {
    display: block;
    width: 328px;
    height: 49px;
    border: 1.5px solid var(--field-border);
    background: transparent;
    color: var(--text-white);
    font-family: "Open Sans", sans-serif;
    font-size: 13px;
    padding: 0 17px;
    outline: none;
  }
  .field::placeholder { color: var(--text-white); opacity: 1; }
  .field + .field { margin-top: 25px; }
  .login-button {
    display: block;
    width: 328px;
    height: 52px;
    margin-top: 31px;
    border: none;
    background: var(--brand-red);
    color: var(--text-white);
    font-family: "Montserrat", sans-serif;
    font-weight: 800;
    font-size: 22px;
    letter-spacing: 0.3px;
    cursor: pointer;
  }
</style>
</head>
<body>
  <main class="login-page">
    <div class="hero-backdrop" role="img" aria-label="Dark night stadium with a footballer in a yellow kit mid-kick and a ball in the air"></div>

    <header class="brand">
      <span class="brand-mark"></span>
      <span class="brand-name">Orbit Field Athletics</span>
    </header>

    <section class="login-frame">
      <div class="login-panel">
        <form class="login-form">
          <input class="field" type="email" placeholder="E mail id">
          <input class="field" type="password" placeholder="Password">
          <button class="login-button" type="button">LOGIN</button>
        </form>
      </div>
      <svg class="corners" viewBox="0 0 422 344" aria-hidden="true">
        <g fill="none" stroke="#e3001b" stroke-width="3">
          <polyline points="1.5,37 1.5,1.5 37,1.5"/>
          <polyline points="385,1.5 420.5,1.5 420.5,37"/>
          <polyline points="1.5,307 1.5,342.5 37,342.5"/>
          <polyline points="385,342.5 420.5,342.5 420.5,307"/>
        </g>
      </svg>
    </section>
  </main>
</body>
</html>
```